New Interrior Decoration company needs new website

We need a website for our new company specialising in interior decoration to residential and commercial markets.
We supply and install decorative and printed films for office and home decoration such as feature walls.
We would like to keep the design simple and clean.

Target Market(s)

Architects and interior designaers

Industry/Entity Type

It Company

Number of Pages Required

5+ page

Font styles to use
Sans Serif

Requirements
Must have
• Home page,
• Services/products page (split into commercial and residential)
• Gallery (split into commercial and residential)
• contact form and page
Nice to have
• Very clean and minimalistic design.

```html
<!DOCTYPE html>
<html lang="en">
<head>
<meta charset="utf-8">
<title>Vantage Interiors</title>
<link rel="stylesheet" href="https://fonts.googleapis.com/css2?family=Arimo:wght@400;700&family=Open+Sans:ital,wght@0,400;0,600;1,400&display=swap">
<style>
:root{
  --blue:#0a56b5;
  --blue-dark:#094c9f;
  --ink:#1b1b1b;
  --muted:#7a7a7a;
  --white:#ffffff;
  --panel:rgba(255,255,255,.85);
  --shade:rgba(60,60,60,.55);
}
*{box-sizing:border-box;margin:0;padding:0}
html,body{width:1200px;height:2880px;overflow:hidden;background:var(--white)}
body{position:relative;font-family:"Open Sans",Arial,sans-serif;color:var(--ink)}
.abs{position:absolute}
h1,h2,h3,h4,.brand,.nav a{font-family:"Arimo",Arial,sans-serif}

/* header */
.site-header{left:0;top:0;width:1200px;height:88px;background:var(--white);border-top:4px solid var(--blue)}
.brand{display:flex;align-items:center;gap:8px;font-weight:700;color:var(--blue);line-height:.95;letter-spacing:-.3px}
.brand .mark{flex:none;background:var(--blue)}
.site-header .brand{left:100px;top:20px;font-size:22px}
.site-header .brand .mark{width:42px;height:42px}
.contact-bar{right:100px;top:16px;display:flex;align-items:center;gap:10px;font-size:15px}
.contact-bar .social{width:20px;height:20px;border-radius:3px;display:inline-block}
.nav{right:100px;top:58px;display:flex;gap:0}
.nav a{font-size:15px;font-weight:700;color:var(--ink);text-decoration:none;padding:0 18px;height:30px;line-height:20px}
.nav a.active{color:var(--blue);border-bottom:3px solid var(--blue)}

/* hero */
.hero{left:0;top:88px;width:1200px;height:450px;background:linear-gradient(180deg,#6f6c68 0%,#8e8a84 40%,#d8d6d2 75%,#b9b6b1 100%)}
.hero-caption{left:282px;top:266px;width:636px;height:88px;background:rgba(70,70,70,.45);text-align:center;color:var(--white)}
.hero-caption h1{font-size:34px;font-weight:700;margin-top:10px}
.hero-caption p{font-size:16px;font-weight:600;margin-top:4px}
.dots{left:550px;top:512px;width:100px;height:26px;background:var(--white);border-radius:50px 50px 0 0;display:flex;justify-content:center;align-items:center;gap:5px}
.dots span{width:10px;height:10px;border-radius:50%;background:#c4c4c4}
.dots span:first-child{background:var(--blue)}

/* welcome */
.section-title{width:1200px;left:0;text-align:center;font-size:27px;font-weight:700;color:var(--ink)}
.welcome-text{left:170px;width:860px;top:644px;text-align:center;font-size:12px;line-height:22px;color:var(--muted)}
.service{width:300px;text-align:center}
.service .photo{width:242px;height:242px;border-radius:50%;margin:0 auto;position:relative}
.service .icon{position:absolute;left:66px;top:66px;width:110px;height:110px;border-radius:50%;background:var(--shade);display:flex;align-items:center;justify-content:center}
.service h3{font-size:18px;font-weight:700;margin-top:25px}
.service p{font-size:12px;line-height:24px;color:var(--muted);margin-top:6px}

/* testimonials */
.testimonials{left:0;top:1115px;width:1200px;height:322px;background:linear-gradient(90deg,#8b8a87 0%,#cfcdc8 35%,#bfb9af 65%,#9a958f 100%)}
.testimonials h2{position:absolute;left:100px;top:40px;color:var(--white);font-size:28px;font-weight:700}
.arrows{position:absolute;right:100px;top:42px;display:flex;gap:6px}
.quote-box{position:absolute;left:100px;top:96px;width:1000px;height:154px;background:var(--panel)}
.quote-mark{position:absolute;left:18px;top:32px;width:90px;height:90px;border-radius:50%;background:#cfcfcf}
.avatar{position:absolute;left:72px;top:32px;width:88px;height:88px;border-radius:50%;background:linear-gradient(160deg,#c9ccd2,#5a6170);border:3px solid var(--white)}
.quote-box p{position:absolute;left:210px;top:20px;width:770px;font-size:14px;font-style:italic;line-height:26px;color:#333}
.quote-box .author{position:absolute;left:210px;top:110px;font-family:"Arimo",Arial,sans-serif;font-weight:700;font-size:15px;color:var(--blue)}

/* works */
.works-grid{left:100px;top:1557px;width:1000px;display:grid;grid-template-columns:repeat(3,327px);grid-auto-rows:246px;gap:10px 9px}
.btn-outline{display:flex;align-items:center;justify-content:center;border:2px solid var(--blue);color:var(--blue);font-size:13px;font-weight:700;font-family:"Arimo",Arial,sans-serif}
.view-more{left:520px;top:2112px;width:160px;height:40px}

/* banner */
.banner{left:0;top:2216px;width:1200px;height:347px;background:linear-gradient(90deg,#cbcbc6 0%,#f1f0ec 30%,#e4e2dd 60%,#c9c7c2 100%)}
.banner-caption{left:207px;top:2333px;width:784px;height:115px;background:rgba(70,70,70,.5);color:var(--white);display:flex;align-items:center;justify-content:center;text-align:center}
.banner-caption h2{font-size:28px;font-weight:700;line-height:38px}

/* footer */
.site-footer{left:0;top:2563px;width:1200px;height:317px;background:var(--blue);color:var(--white)}
.site-footer .brand{position:absolute;left:100px;top:104px;font-size:27px;color:var(--white)}
.site-footer .brand .mark{width:52px;height:52px;background:var(--white)}
.footer-col{position:absolute;top:40px}
.footer-col h4{font-size:18px;font-weight:700;margin-bottom:18px}
.footer-col li{list-style:none;font-size:12px;line-height:29px}
.footer-col p{font-size:12px;line-height:21px}
.email-field{margin-top:14px;width:264px;height:34px;background:var(--white);color:#777;font-size:12px;padding:9px 14px}
.subscribe{margin-top:12px;width:102px;height:34px;border-color:var(--white);color:var(--white)}
.contact-row{display:flex;gap:16px;font-size:12px;line-height:19px;margin-bottom:18px}
.copyright{position:absolute;left:100px;top:271px;font-size:12px}
.footer-social{position:absolute;left:950px;top:264px;display:flex;gap:8px}
.footer-social span{width:32px;height:32px;border-radius:50%;border:2px solid var(--white)}
</style>
</head>
<body>

<header class="site-header abs">
  <div class="brand abs"><span class="mark"></span><span>VANTAGE<br>INTERIORS</span></div>
  <div class="contact-bar abs">
    <svg width="20" height="18" viewBox="0 0 20 18"><rect width="20" height="18" rx="3" fill="#0a56b5"/><path d="M4 5l6 5 6-5" stroke="#fff" stroke-width="1.6" fill="none"/></svg>
    <span>info@vantageinteriors.com</span>
    <svg width="20" height="20" viewBox="0 0 20 20" style="margin-left:14px"><rect width="20" height="20" rx="3" fill="#0a56b5"/><path d="M6 4c-1 1-1 3 1 6s4 5 6 6c1 0 2-1 2-2l-2-2-2 1-3-3 1-2-2-2z" fill="#fff"/></svg>
    <span>1 800 555 0142</span>
    <span class="social" style="background:#3b5998;margin-left:6px"></span>
    <span class="social" style="background:#1da1f2"></span>
    <span class="social" style="background:#0e76a8"></span>
    <span class="social" style="background:#a9785c"></span>
  </div>
  <nav class="nav abs">
    <a class="active">HOME</a><a>SERVICES</a><a>PRODUCTS</a><a>GALLERY</a><a>CONTACT US</a>
    <a><svg width="14" height="14" viewBox="0 0 14 14"><circle cx="6" cy="6" r="4.5" stroke="#1b1b1b" stroke-width="2" fill="none"/><path d="M9 9l4 4" stroke="#1b1b1b" stroke-width="2"/></svg></a>
  </nav>
</header>

<section class="hero abs" role="img" aria-label="Modern kitchen interior with white island, pendant lamps and timber cabinetry"></section>
<div class="hero-caption abs">
  <h1>VANTAGE INTERIORS</h1>
  <p>We specialise in interior decoration to residential and commercial markets.</p>
</div>
<div class="dots abs"><span></span><span></span><span></span><span></span><span></span></div>

<h2 class="section-title abs" style="top:595px">WELCOME TO VANTAGE INTERIORS</h2>
<p class="welcome-text abs">Sed ut perspiciatis unde omnis iste natu accusantium doloremque laudantium, totam rem aperiam, eaque ipsa quae ab illo inventore veritatis et quasi architecto beatae vitae dicta sunt expur aut odit aut fug quia consequuntur magni dolores eos qui ratione voluptatem sequi</p>

<div class="service abs" style="left:90px;top:724px">
  <div class="photo" role="img" aria-label="Residential living room interior" style="background:radial-gradient(circle,#e8ecd0,#b7c46a 60%,#8a9a3c)">
    <span class="icon"><svg width="50" height="46" viewBox="0 0 50 46"><path d="M25 3L3 23h7v20h11V30h8v13h11V23h7z" fill="#fff"/></svg></span>
  </div>
  <h3>Residential Interior Design</h3>
  <p>At vero eos et accusamus et iusto odio dignissimos duc imus qui blanditiis praesentiumvo</p>
</div>
<div class="service abs" style="left:450px;top:724px">
  <div class="photo" role="img" aria-label="Commercial office interior with yellow panels" style="background:radial-gradient(circle,#f0e2bd,#d9a536 60%,#8d6a2b)">
    <span class="icon"><svg width="36" height="50" viewBox="0 0 36 50"><rect x="3" y="3" width="30" height="44" fill="none" stroke="#fff" stroke-width="3"/><g fill="#fff"><rect x="9" y="9" width="6" height="6"/><rect x="21" y="9" width="6" height="6"/><rect x="9" y="20" width="6" height="6"/><rect x="21" y="20" width="6" height="6"/><rect x="9" y="31" width="6" height="6"/><rect x="21" y="31" width="6" height="6"/></g></svg></span>
  </div>
  <h3>Commercial Interior Design</h3>
  <p>At vero eos et accusamus et iusto odio dignissimos duc imus qui blanditiis praesentiumvo</p>
</div>
<div class="service abs" style="left:808px;top:724px">
  <div class="photo" role="img" aria-label="Office glass partition with decorative printed film" style="background:radial-gradient(circle,#e6e3df,#b9b1a6 60%,#8d7a63)">
    <span class="icon"><svg width="50" height="50" viewBox="0 0 50 50"><circle cx="20" cy="27" r="11" fill="none" stroke="#fff" stroke-width="6" stroke-dasharray="5 3"/><circle cx="20" cy="27" r="4" fill="#fff"/><circle cx="37" cy="13" r="7" fill="none" stroke="#fff" stroke-width="4" stroke-dasharray="3 2"/></svg></span>
  </div>
  <h3>Supply and Installation</h3>
  <p>At vero eos et accusamus et iusto odio dignissimos duc imus qui blanditiis praesentiumvo</p>
</div>

<section class="testimonials abs" role="img" aria-label="Bright concrete office interior with timber desk">
  <h2>TESTIMONIALS</h2>
  <div class="arrows">
    <svg width="22" height="22" viewBox="0 0 22 22"><circle cx="11" cy="11" r="10" fill="#fff"/><path d="M13 6l-5 5 5 5" stroke="#777" stroke-width="2.4" fill="none"/></svg>
    <svg width="22" height="22" viewBox="0 0 22 22"><circle cx="11" cy="11" r="10" fill="#fff"/><path d="M9 6l5 5-5 5" stroke="#777" stroke-width="2.4" fill="none"/></svg>
  </div>
  <div class="quote-box">
    <span class="quote-mark"></span>
    <span class="avatar" role="img" aria-label="Client portrait"></span>
    <p>It is a long established fact that a reader will be distracted by the readable content of a page when looking at its layout. The point of using Lorem Ipsum is that it has a more-or-less normal distribution of letters, as opposed to using 'Content here, content here', making it look like readable English.</p>
    <span class="author">DANIEL REYES</span>
  </div>
</section>

<h2 class="section-title abs" style="top:1494px">OUR WORKS</h2>
<div class="works-grid abs">
  <div role="img" aria-label="Lounge chair in dark red room with bookshelf" style="background:linear-gradient(135deg,#3a1a14,#7a3020 55%,#d8c8d8)"></div>
  <div role="img" aria-label="White sofa against grey wall" style="background:linear-gradient(180deg,#5e5e5c,#8a8986 65%,#dcdcd9)"></div>
  <div role="img" aria-label="Grey kitchen with pendant lamps and window" style="background:linear-gradient(135deg,#8f918e,#c9cbc7 55%,#4c4f4e)"></div>
  <div role="img" aria-label="Olive green wall with low sideboard" style="background:linear-gradient(180deg,#7d7948,#a19c64 65%,#d9d6c2)"></div>
  <div role="img" aria-label="Colourful timber feature wall with red armchairs" style="background:linear-gradient(90deg,#b78b4a,#d9b56a 45%,#c44b2f 80%,#e2ddd0)"></div>
  <div role="img" aria-label="Plum wall with white sectional sofa" style="background:linear-gradient(180deg,#5b2a38,#7e4152 60%,#e5ddd2)"></div>
</div>
<div class="btn-outline view-more abs">VIEW MORE &gt;&gt;</div>

<section class="banner abs" role="img" aria-label="Glass office partitions with printed decorative film"></section>
<div class="banner-caption abs"><h2>We supply and install decorative and printed films for<br>office and home decoration</h2></div>

<footer class="site-footer abs">
  <div class="brand"><span class="mark"></span><span>VANTAGE<br>INTERIORS</span></div>
  <div class="footer-col" style="left:438px">
    <h4>INFORMATION</h4>
    <ul><li>Home</li><li>Services</li><li>Products</li><li>Gallery</li><li>Contact us</li></ul>
  </div>
  <div class="footer-col" style="left:614px">
    <h4>NEWSLETTER</h4>
    <p>Register your email address to get<br>information about us</p>
    <div class="email-field">Email Address</div>
    <div class="btn-outline subscribe">SUBSCRIBE</div>
  </div>
  <div class="footer-col" style="left:929px">
    <h4>CONTACT US</h4>
    <div class="contact-row"><svg width="10" height="14" viewBox="0 0 10 14"><path d="M5 0a5 5 0 0 0-5 5c0 4 5 9 5 9s5-5 5-9a5 5 0 0 0-5-5z" fill="#fff"/><circle cx="5" cy="5" r="2" fill="#0a56b5"/></svg><span>418 Linden Avenue |<br>Suite 200-B<br>Maple Grove, CA 90455</span></div>
    <div class="contact-row"><svg width="12" height="12" viewBox="0 0 20 20"><path d="M4 1C2 3 2 6 5 11s7 8 10 8c2 0 3-2 3-3l-3-3-3 1-5-5 1-3z" fill="#fff"/></svg><span>1 800 555 0142</span></div>
    <div class="contact-row"><svg width="13" height="10" viewBox="0 0 13 10"><rect width="13" height="10" fill="#fff"/><path d="M0 0l6.5 5L13 0" stroke="#0a56b5" fill="none"/></svg><span>info@vantageinteriors.com</span></div>
  </div>
  <div class="copyright">Copyrights © 2016, Vantage Interiors.  All rights reserved.</div>
  <div class="footer-social"><span></span><span></span><span></span><span></span></div>
</footer>

</body>
</html>
```